Business Cards for a company that provides webstore services to veterinarians

We need business cards designed for our main service PawCartHub. PawCartHub is a webstore that veterinarian clinics can use to that will allow their clients to purchase products for their pets. Our company is Brindlow Veterinary Solutions (Brindlow Veterinary Solutions). Our mission statement is We love pets! We will do everything possible to facilitate along, healthy and happy relationship with their families.

Target Market(s)

Veterinarians

Industry/Entity Type

Veterinary

Contact Information for Business Card

I would like the design to incorporate the colours our our company. Cards should have room for employee name, title (only necessary in two instances), phone number, mobile number, email address and linkedin symbol and related profile name ie Marla Quinton. I would like the PawCartHub logo to appear on one side and Brindlow Veterinary Solutions logo to appear on the other. I will need both an english and french version. I can provide the french translation. Please focus on english version and then we will translate

Colors

Designer to choose colors to be used in the design.

Requirements
Must have
• one side - PawCartHub logo with persons name, phone number, mobile number, email address
• second side - Brindlow Veterinary Solutions logo
• colours should be consistent with our company. colours are as follows:
• Red
• RGB: 190 / 30 / 45
• CYMK: 14 / 100 / 90 /10
• Hex: #BE1E2D
• Gray
• RGB: 88 / 89 / 86
• CYMK: 3 / 2 / 0 /64
• Hex: #585956
Nice to have
• address of company - can be on either side address is 4817 Feldmoor Street Suite 305 Burlington ON K2R 6T4. Toll free number will vary depending on person
• Linkedin symbol and name of person
• on second side with Brindlow Veterinary Solutions logo our company's mission statement
Should not have
• nothing comes to mind

```html
<!DOCTYPE html>
<html lang="en">
<head>
<meta charset="utf-8">
<title>PawCartHub Business Card</title>
<link rel="stylesheet" href="https://fonts.googleapis.com/css2?family=Bebas+Neue&family=Open+Sans:wght@400;600&family=Montserrat:wght@400;600&display=swap">
<style>
  :root {
    --brand-red: #be1e2d;
    --brand-gray: #585956;
    --gray-light: #6b6c69;
    --ink: #4a4b48;
    --paper: #ffffff;
    --stage: #e9e9e7;
    --placeholder: #7a7b78;
    --on-dark: #f2f2f2;
  }
  * { box-sizing: border-box; margin: 0; padding: 0; }
  html, body { width: 1200px; height: 900px; overflow: hidden; }
  body {
    background: var(--stage);
    font-family: "Open Sans", Arial, sans-serif;
    position: relative;
  }
  .card {
    position: absolute;
    left: 250px;
    width: 700px;
    height: 400px;
    overflow: hidden;
    box-shadow: 0 6px 18px rgba(0,0,0,.18);
  }
  /* Back side */
  .card--back {
    top: 35px;
    background: linear-gradient(160deg, var(--gray-light), var(--brand-gray));
    color: var(--on-dark);
    text-align: center;
  }
  .brand-art {
    position: absolute;
    left: 275px; top: 50px;
    width: 150px; height: 100px;
    background: var(--placeholder);
    border-radius: 6px;
  }
  .company-name {
    position: absolute;
    left: 0; right: 0; top: 176px;
    font-family: "Montserrat", Arial, sans-serif;
    font-weight: 600;
    font-size: 30px;
    letter-spacing: 1px;
    color: #e6e6e6;
    white-space: nowrap;
  }
  .profile {
    position: absolute;
    left: 0; right: 0; top: 262px;
    font-family: "Montserrat", Arial, sans-serif;
    font-size: 15px;
    display: flex; justify-content: center; align-items: center; gap: 10px;
  }
  .profile__mark { width: 12px; height: 12px; background: var(--on-dark); }
  .mission {
    position: absolute;
    left: 0; right: 0; top: 300px;
    font-family: "Montserrat", Arial, sans-serif;
    font-size: 22px;
    letter-spacing: 3px;
  }
  /* Front side */
  .card--front {
    top: 465px;
    background: var(--paper);
  }
  .brand-name {
    position: absolute;
    left: 0; right: 0; top: 68px;
    text-align: center;
    font-size: 54px;
    font-weight: 400;
    color: var(--brand-gray);
    letter-spacing: -1px;
    white-space: nowrap;
  }
  .person {
    position: absolute;
    left: 40px; top: 180px;
    width: 290px;
    text-align: right;
  }
  .person__name {
    font-family: "Bebas Neue", Impact, sans-serif;
    font-size: 50px;
    line-height: 1;
    color: var(--brand-red);
    white-space: nowrap;
  }
  .person__title {
    font-size: 17px;
    letter-spacing: 2px;
    color: var(--ink);
    margin-top: 2px;
  }
  .divider {
    position: absolute;
    left: 360px; top: 170px;
    width: 2px; height: 118px;
    background: var(--brand-red);
  }
  .contacts {
    position: absolute;
    left: 392px; top: 166px;
    list-style: none;
    font-size: 16px;
    color: var(--ink);
    line-height: 25px;
    white-space: nowrap;
  }
  .contacts li { display: flex; align-items: center; gap: 14px; }
  .contacts svg { width: 13px; height: 13px; flex: none; }
  .address-band {
    position: absolute;
    left: 0; right: 0; bottom: 0;
    height: 46px;
    background: var(--brand-gray);
    color: var(--on-dark);
    font-size: 17px;
    display: flex; align-items: center; justify-content: center;
    white-space: nowrap;
  }
</style>
</head>
<body>

<section class="card card--back" aria-label="Back of card">
  <div class="brand-art" role="img" aria-label="Heart outline framing a seated person with a cat and a dog"></div>
  <div class="company-name">Brindlow Veterinary Solutions</div>
  <div class="profile"><span class="profile__mark"></span>@Marla Quinton</div>
  <div class="mission">We love pets!</div>
</section>

<section class="card card--front" aria-label="Front of card">
  <div class="brand-name">pawcarthub.ca</div>

  <div class="person">
    <div class="person__name">Marla Quinton</div>
    <div class="person__title">DIRECTOR</div>
  </div>

  <div class="divider"></div>

  <ul class="contacts">
    <li>
      <svg viewBox="0 0 16 16"><path d="M2 6c2-3 10-3 12 0l-2 2-2-1V5H6v2L4 8z" fill="#be1e2d"/><rect x="4" y="9" width="8" height="5" rx="1" fill="#be1e2d"/></svg>
      +330 4102-5538
    </li>
    <li>
      <svg viewBox="0 0 16 16"><rect x="4" y="1" width="8" height="14" rx="1.5" fill="none" stroke="#be1e2d" stroke-width="1.6"/></svg>
      +330 4167-2904
    </li>
    <li>
      <svg viewBox="0 0 16 16"><path d="M4 1l3 3-2 2c1 2 3 4 5 5l2-2 3 3-2 3C7 14 2 9 1 4z" fill="#be1e2d"/></svg>
      +330 4089-3315 (Toll free)
    </li>
    <li>
      <svg viewBox="0 0 16 16"><rect x="1" y="3" width="14" height="10" fill="none" stroke="#be1e2d" stroke-width="1.6"/><path d="M1 3l7 6 7-6" fill="none" stroke="#be1e2d" stroke-width="1.6"/></svg>
      info@pawcarthub.com
    </li>
    <li>
      <svg viewBox="0 0 16 16"><circle cx="8" cy="8" r="6.5" fill="none" stroke="#be1e2d" stroke-width="1.4"/><path d="M1.5 8h13M8 1.5c-3 3-3 10 0 13M8 1.5c3 3 3 10 0 13" fill="none" stroke="#be1e2d" stroke-width="1.2"/></svg>
      www.pawcarthub.com
    </li>
  </ul>

  <div class="address-band">4817 Feldmoor Street Suite 305 Burlington ON K2R 6T4.</div>
</section>

</body>
</html>
```